Newsletter template for Mortgage Broking business

Require a newsletter design/template to be used for specific loan products. Example of existing newsletter attached. Need it to look sharper and more effective. Require a couple of templates for both ongoing regular newsletters as well as special offer type newsletters. Currently use YMLP as my newsletter mail out program - so it needs to be compatible with this. Have attached logos and some image files also.

Loan

```html
<!DOCTYPE html>
<html lang="en">
<head>
<meta charset="utf-8">
<title>Marlowe Lending Solutions – SMSF Commercial Update</title>
<link href="https://fonts.googleapis.com/css2?family=Ubuntu:wght@400;500;700&display=swap" rel="stylesheet">
<style>
:root{
  --bar:#6d6d6d;
  --ink:#2f2f2f;
  --body:#555;
  --link:#1a66b3;
  --brand:#4a2a78;
  --phone:#1d5f8c;
  --blue-top:#3d98d6;
  --blue-bot:#1f6fb0;
  --purple-top:#7a5ea0;
  --purple-bot:#4b3372;
  --rate:#2a7fc0;
  --red:#d0111b;
  --cream:#fffde3;
  --rule:#d6d6d6;
  --bullet:#2f86c6;
}
*{box-sizing:border-box;margin:0;padding:0}
html,body{width:720px;height:1200px;overflow:hidden;background:#fff}
body{font-family:"Ubuntu",sans-serif;color:var(--body);position:relative}
a{color:var(--link)}
.top-bar,.bottom-bar{position:absolute;left:0;width:720px;height:19px;background:var(--bar);color:#fff;font-size:11px;text-align:center;line-height:19px}
.top-bar{top:0}
.bottom-bar{bottom:0}
.bottom-bar a{color:#fff}
.header{position:absolute;top:28px;left:80px;width:560px;height:62px}
.brand{position:absolute;left:4px;top:14px;font-size:22px;font-weight:500;color:var(--brand);display:flex;align-items:center;gap:7px}
.brand-dot{width:12px;height:12px;border-radius:50%;background:var(--brand)}
.contact{position:absolute;right:0;top:6px;text-align:left;color:var(--ink)}
.contact .label{font-size:11.5px}
.contact .phone{font-size:25px;font-weight:700;color:var(--phone);line-height:25px;letter-spacing:.5px}
.contact .note{font-size:11.5px}
.hero{position:absolute;top:93px;left:80px;width:560px;height:191px;border-top:2px solid #555;background:linear-gradient(160deg,#f4f4f4,#dcdfe3 60%,#b9bec6)}
.hero-caption{position:absolute;left:0;bottom:6px;width:293px;height:59px;background:#2a2d31;clip-path:polygon(0 0,88% 0,100% 100%,0 100%);color:#fff;font-size:19px;line-height:23px;padding:6px 10px}
.hero-caption strong{color:#8fd0f5;font-weight:500}
.col-left{position:absolute;top:290px;left:80px;width:183px}
.col-right{position:absolute;top:290px;left:280px;width:360px}
.side-block{border-bottom:1px solid var(--rule);padding-bottom:9px;margin-bottom:7px}
.side-title{font-size:12px;font-weight:500;color:var(--ink);line-height:14.5px;margin-bottom:6px}
.side-text{font-size:10px;line-height:14.4px;margin-bottom:8px}
.side-link{font-size:10.4px;line-height:14.5px;display:block}
.photo-trucks{width:183px;height:92px;background:linear-gradient(#8aa3c4,#4a5a72 55%,#2d3138);margin:6px 0 9px}
.asset-list{list-style:none;font-size:10px;line-height:16px;margin:8px 0 6px}
.asset-list li,.feature-list li,.param-list li{position:relative;padding-left:18px}
.asset-list li::before,.feature-list li::before,.param-list li::before{content:"";position:absolute;left:4px;top:5.5px;width:5px;height:5px;border-radius:50%;background:var(--bullet)}
.btn{display:block;text-align:center;color:#fff;text-decoration:none;background:linear-gradient(var(--purple-top),var(--purple-bot));border-radius:4px;border:1px solid #3a2560}
.btn-forward{width:175px;height:49px;font-size:16px;line-height:19px;padding-top:5px;margin-top:8px}
.offer-box{height:93px;background:linear-gradient(var(--blue-top),var(--blue-bot));border:1px solid #1a5a90;color:#fff;padding:7px 8px;font-size:15.5px;line-height:20px}
.offer-box strong{font-size:16px;font-weight:500}
.rates{background:#f7f7f7;padding:12px 0 10px;text-align:center}
.rates-title{font-size:12.5px;color:#555;font-weight:500}
.rates-title span{color:var(--rate)}
.rate-grid{display:flex;justify-content:center;align-items:center;gap:8px;margin:10px 0 8px}
.rate-list{font-size:12.5px;line-height:17.5px;color:#333;text-align:right}
.rate-list span{color:var(--rate)}
.no-fee{color:var(--red);font-size:13px}
.btn-submit{width:295px;height:32px;margin:0 auto;font-size:15.5px;line-height:31px}
.params{background:var(--cream);margin-top:5px;padding:8px 9px 8px;height:200px}
.params h2{font-size:14.5px;font-weight:500;color:var(--ink);margin-bottom:7px}
.param-list{list-style:none;font-size:10px;line-height:14.5px}
.doc-options{color:var(--rate);font-size:12px;line-height:14.5px;margin:6px 0 9px 8px}
.lmi-head{margin-top:10px;font-size:15px;color:#444;font-weight:500}
.lmi-sub{font-size:10.6px;color:#333;margin-top:2px}
.photo-form{height:156px;margin-top:7px;border:2px solid #8a8a8a;background:linear-gradient(100deg,#c9a26a 0 8%,#efefef 8%,#dcdcdc 70%,#b8b8b8)}
.detectives{margin-top:13px;font-size:14px;color:#444;font-weight:500}
.para{font-size:10px;line-height:13px;color:#444;margin-top:9px}
.feature-list{list-style:none;font-size:10px;line-height:14.5px;color:#444;margin-top:7px}
</style>
</head>
<body>
<div class="top-bar">April 2014 Update - SMSF COMMERCIAL &nbsp; PRODUCT = 70% LVR 6.99%!!!!</div>

<header class="header">
  <div class="brand"><span class="brand-dot"></span>Marlowe Lending Solutions</div>
  <div class="contact">
    <div class="label">Call us free on</div>
    <div class="phone">0800 555 019</div>
    <div class="note">for fiendly advice and suport</div>
  </div>
</header>

<section class="hero" role="img" aria-label="Photo of a mortgage application form stamped approved with a house keyring">
  <div class="hero-caption">SMSF, Low Doc &amp; Credit<br>Impaired <strong>SPECIALIST LOANS</strong></div>
</section>

<aside class="col-left">
  <div class="side-block">
    <h3 class="side-title">Has an application been declined by LMI due to credit scoring? New 95% Full Doc - NO LMI!!!</h3>
    <p class="side-text">New 95% LVR Full Doc Loans - no credit scoring, no LMI. (must be clean credit applications - can have multiple enquiries)</p>
    <a class="side-link" href="#">Submit your Loan enquiry here</a>
  </div>
  <div class="side-block">
    <h3 class="side-title">Premium Low Doc!</h3>
    <p class="side-text">Low Doc 80% Interest Rate at <a href="#">6.24%</a><br>Impairments under $750 ignored!</p>
    <a class="side-link" href="#">Submit your Low Doc enquiry here</a>
  </div>
  <div class="side-block">
    <h3 class="side-title">Bad Credit?</h3>
    <p class="side-text">Credit Impaired Loans from 5.45% 1 day discharged bankrupts considered. Multiple defaults, paid &amp; unpaid.</p>
    <a class="side-link" href="#">Submit your Bad Credit Loan enquiry here</a>
  </div>
  <h3 class="side-title">Private Money starting from 8% available for unregulated deals and development funding!!!</h3>
  <div class="photo-trucks" role="img" aria-label="Photo of three trucks on a highway at dusk"></div>
  <h3 class="side-title">Car &amp; Asset Finance</h3>
  <p class="side-text">Low Doc &amp; No Doc finance is available for a wide variety of assets including;</p>
  <ul class="asset-list">
    <li>Motor Vehicles</li>
    <li>Fit-Out Finance</li>
    <li>Plant &amp; Equipment</li>
    <li>Caravans, Trucks,</li>
    <li>Heavy Vehicles up to 4.5 tonnes with no financials</li>
    <li>ATMs, Gaming Machines</li>
    <li>Vending Machines</li>
    <li>Taxis, VHA vehicles etc</li>
    <li>Medical &amp; AV &amp; Sound Equipment</li>
    <li>POS Systems, Photographic equip-ment</li>
    <li>Coffee Machines, Printing equip-ment</li>
  </ul>
  <p class="side-text">Just about anything with a serial number!</p>
  <a class="side-link" href="#">Submit your car or asset enquiry here</a>
  <a class="btn btn-forward" href="#">Forward this email<br>to a friend</a>
</aside>

<main class="col-right">
  <div class="offer-box"><strong>NEW RES SMSF PRODUCT - 5.60% at 80%!</strong><br>YES - 80% LVR!! 100% rental income allowed for servicing, some minor impairments considered.</div>

  <div class="rates">
    <div class="rates-title">Prime Low Doc - Rates Slashed! &nbsp;<span>No risk fee up to 70%!</span></div>
    <div class="rate-grid">
      <div class="rate-list">
        <div><span>80%</span> LVR - <span>5.65%</span></div>
        <div><span>75%</span> LVR - <span>5.55%</span></div>
        <div><span>70%</span> LVR - <span>5.45%</span></div>
      </div>
      <svg width="14" height="54" viewBox="0 0 14 54" aria-hidden="true"><path d="M2 2 Q8 2 8 10 V22 Q8 27 13 27 Q8 27 8 32 V44 Q8 52 2 52" fill="none" stroke="#999" stroke-width="1.5"/></svg>
      <div class="no-fee">No Risk Fee!!</div>
    </div>
    <a class="btn btn-submit" href="#">SUBMIT YOUR SCENARIO HERE!</a>
  </div>

  <section class="params">
    <h2>Key product parameters are:</h2>
    <ul class="param-list">
      <li>Unlimited cash out (with written purpose from borrower)</li>
      <li>No Business debt consol</li>
      <li>2 yr ABN required</li>
      <li>Low Doc Dec and 2 of the following:</li>
    </ul>
    <div class="doc-options">Accountants Declaration;<br>BAS Statements;<br>Biz Bank Statements.</div>
    <ul class="param-list">
      <li>Max Loan amount at 70% $2mil!!</li>
      <li>Max Loan amount at 75% $1.5mil!!</li>
      <li>Max Loan amount at 80% $1mil!!</li>
    </ul>
  </section>

  <h2 class="lmi-head">NO LMI, NO RISK FEE (At 70% LVR)</h2>
  <p class="lmi-sub">Cat 1-4 allowed. max 25 acres! Vacant Land on Cat 1 &amp; 2 locations!!</p>
  <div class="photo-form" role="img" aria-label="Photo of a loan application form stamped approved with a pen"></div>

  <h2 class="detectives">The Mortgage Detectives....</h2>
  <p class="para">At Marlowe Lending Solutions we have access to niche non-conforming lenders who offer our clients &amp; yours flexibility and solutions where others cannot.</p>
  <p class="para">Some of the key features of our loans include</p>
  <ul class="feature-list">
    <li>Low doc 60-80% loans with minimal or no risk fees, no LMI, unlimited cash out &amp; no financials required</li>
    <li>95% Loan to Value with no LMI and allowance for credit impairments (Full doc max LVR 95%; Low Doc Max LVR 85%)</li>
    <li>Debt Consolidation (including ATO debts)</li>
    <li>No BAS or trading statements required for 80% Low Doc loans</li>
    <li>90% Low Doc available</li>
    <li>Self certification/ declaration of income &amp; accountants letter only for low doc loans</li>
  </ul>
</main>

<div class="bottom-bar"><a href="#">Click here</a> to view this email in your browser</div>
</body>
</html>
```